Plakat-Design zum Thema: Kuchen der Saison
Zielgruppe
Wer wir sind:
Das Campusdienst Velmerau betreut im Auftrag des Landes Baden-Württemberg in Karlsruhe und Pforzheim circa 48.000 Studierende in allen Fragen rund um das Studium. Bei uns sind alle Studierenden richtig, wenn Sie...
- BAföG beantragen wollen oder Beratung bei der Studienfinanzierung brauchen,
- Einen Platz im Studentenwohnheim suchen,
- in Mensen und Cafeterien essen wollen,
- rechtliche Probleme haben (Erstberatung),
- ein Studienabschlussdarlehen benötigen,
- einen Platz in einer Kinderbetreuungseinrichtung benötigen,
- an studentischer Kultur interessiert sind,
- kostenlose psychotherapeutische Beratung suchen.
www.cd-vlm.de
Unsere Zielgruppe:
Unsere Zielgruppe sind primär Studierende im Alter von 20 - 30 Jahren, überwiegend männlich.
Aufgabenstellung
Plakatgröße: DIN A 1
Thema: 'Kuchen der Saison'
Plakat in unseren Cafeterien im Zeitraum Mai/Juni. Keine Zeitangabe auf das Plakat. Folgende Kuchen sollen beworben werden:
Erdbeere
Heidelbeere
Apfel
Pflaume
Kirsch
Rhabarber
Linzer
Hintergrundinfo: die Kuchen kommen von einer Bäckerei aus Karlsruhe…vielleicht ist das für die Gestaltung interessant…regional, frisch, Handwerk….
Es geht also nicht um eine Rabatt-Aktion o.ä. sondern um die 'Kuchen der Saison' an sich.
Da man aber nicht weiß, wie das Wetter mitspielt und die Ernte ausfällt, muss das Plakat 'oberflächlich' sein und nicht auf einen bestimmten Kuchen abzielen.
Das MUSS aufs Plakat:
- Bitte Verwendung unserer Plakatvorlage.
- Bitte Einhaltung unserer CI.

```html
<!DOCTYPE html>
<html lang="de">
<head>
<meta charset="utf-8">
<title>Kuchen der Saison – Plakat</title>
<link rel="stylesheet" href="https://fonts.googleapis.com/css2?family=Lobster&family=Alegreya+Sans:wght@800&display=swap">
<style>
  :root {
    --bg: #ececec;
    --paper: #f8f8f8;
    --green: #7aab2e;
    --cyan: #00a6d6;
    --blue: #5587c6;
    --orange: #d96516;
    --red: #b31b1b;
    --purple: #62457c;
    --yellow: #ffe600;
    --black: #000000;
    --ink: #111111;
    --white: #ffffff;
    --url-grey: #a8a8a8;
    --badge-grey: #9b9b9b;
    --fruit-red: #d23a3c;
    --fruit-cherry: #9e1f2c;
    --fruit-blue: #3b4a6b;
  }
  * { margin: 0; padding: 0; box-sizing: border-box; }
  html, body { width: 1200px; height: 1200px; overflow: hidden; background: var(--bg); }
  .poster {
    position: absolute; left: 216px; top: 56px;
    width: 768px; height: 1087px;
    background: var(--paper); overflow: hidden;
  }

  /* Kopfleiste */
  .header-bands { position: absolute; left: 0; top: 0; width: 768px; height: 166px; }
  .band { position: absolute; height: 83px; }
  .band.row-1 { top: 0; } .band.row-2 { top: 83px; }
  .band.col-1 { left: 0; width: 263px; }
  .band.col-2 { left: 263px; width: 240px; }
  .band.col-3 { left: 503px; width: 265px; }
  .brand {
    position: absolute; left: 263px; width: 240px; top: 83px; height: 83px;
    display: flex; justify-content: center; align-items: center; gap: 10px;
    font-family: "Alegreya Sans", sans-serif; font-weight: 800;
    font-size: 21px; line-height: 22px; color: var(--white);
  }
  .brand-square { width: 16px; height: 16px; background: var(--yellow); flex: none; }

  /* Bildfläche */
  .photo {
    position: absolute; left: 0; top: 166px; width: 768px; height: 858px;
    background: linear-gradient(160deg, #fbfbfb 0%, #f2f2f2 100%);
  }
  .fruit-plate {
    position: absolute; left: 0; top: 348px; width: 372px; height: 500px;
    border-radius: 0 250px 250px 0;
    background: linear-gradient(135deg, var(--fruit-blue) 0%, var(--fruit-cherry) 40%, var(--fruit-red) 75%, #e9a3a0 100%);
  }
  .fruit-scatter {
    position: absolute; left: 195px; top: 870px; width: 110px; height: 120px;
    border-radius: 45%;
    background: linear-gradient(160deg, #e0464a, #c92f33);
  }

  /* Typografie */
  .headline {
    position: absolute; left: 56px; top: 158px;
    font-family: "Lobster", cursive; font-weight: 400;
    font-size: 172px; line-height: 1; color: var(--green);
  }
  .subline {
    position: absolute; left: 332px; top: 282px;
    font-family: "Lobster", cursive; font-size: 88px; line-height: 1;
    color: var(--ink);
  }
  .cake-list {
    position: absolute; left: 518px; top: 555px; list-style: none;
    font-family: "Alegreya Sans", sans-serif; font-weight: 800;
    font-size: 38px; line-height: 41px; color: var(--ink);
  }
  .cake-list li::before { content: "•"; margin-right: 2px; }

  .partner-badge {
    position: absolute; left: 669px; top: 913px; width: 78px; height: 103px;
    background: var(--badge-grey);
  }

  /* Fußleiste */
  .footer-stripe { position: absolute; left: 0; top: 1024px; width: 768px; height: 6px; }
  .stripe { position: absolute; top: 0; height: 6px; }
  .footer-bar {
    position: absolute; left: 0; top: 1030px; width: 768px; height: 57px;
    background: var(--black);
    display: flex; justify-content: center; align-items: center;
    font-family: "Alegreya Sans", sans-serif; font-weight: 800;
    font-size: 25px; color: var(--url-grey); letter-spacing: 0.5px;
  }
</style>
</head>
<body>
  <div class="poster">
    <div class="photo" role="img" aria-label="Foto: weißer Holztisch mit einzelnen Kirschen, Beeren und Minzblättern"></div>
    <div class="fruit-plate" role="img" aria-label="Foto: weißer Teller voller Erdbeeren, Heidelbeeren und Kirschen mit Minze"></div>
    <div class="fruit-scatter" role="img" aria-label="Foto: halbe Erdbeere auf dem Tisch"></div>

    <div class="header-bands">
      <div class="band row-1 col-1" style="background:var(--green)"></div>
      <div class="band row-1 col-2" style="background:var(--cyan)"></div>
      <div class="band row-1 col-3" style="background:var(--blue)"></div>
      <div class="band row-2 col-1" style="background:var(--orange)"></div>
      <div class="band row-2 col-2" style="background:var(--red)"></div>
      <div class="band row-2 col-3" style="background:var(--purple)"></div>
      <div class="brand"><span class="brand-square"></span><span>Campusdienst<br>Velmerau</span></div>
    </div>

    <h1 class="headline">Kuchen</h1>
    <p class="subline">der Saison</p>

    <ul class="cake-list">
      <li>Erdbeere</li>
      <li>Heidelbeere</li>
      <li>Apfel</li>
      <li>Pflaume</li>
      <li>Kirsch</li>
      <li>Rhabarber</li>
      <li>Linzer</li>
    </ul>

    <div class="partner-badge"></div>

    <div class="footer-stripe">
      <span class="stripe" style="left:0;width:82px;background:var(--green)"></span>
      <span class="stripe" style="left:82px;width:61px;background:var(--cyan)"></span>
      <span class="stripe" style="left:143px;width:61px;background:var(--blue)"></span>
      <span class="stripe" style="left:204px;width:46px;background:var(--black)"></span>
      <span class="stripe" style="left:250px;width:272px;background:var(--yellow)"></span>
      <span class="stripe" style="left:522px;width:42px;background:var(--black)"></span>
      <span class="stripe" style="left:564px;width:61px;background:var(--orange)"></span>
      <span class="stripe" style="left:625px;width:61px;background:var(--red)"></span>
      <span class="stripe" style="left:686px;width:82px;background:var(--purple)"></span>
    </div>
    <div class="footer-bar">www.cd-vlm.de</div>
  </div>
</body>
</html>
```